【 概要 】 支援しているクライアントのクリニックの公式PIROのリッチメニューのデザインを募集します。 【 依頼内容 】 ・PIROリッチメニュー(2×3) ・作成数: 1種類 ・設定予定の項目 └Web受付・予約 └Free Wi-Fi └公式サイト └診療カレンダー └よくある質問 └お問い合わせ 【 デザインイメージ 】 ・メインターゲット:30~50代 女性(幅広い年齢層の患者さんがいます) ・雰囲気:水色ベースでユーザーが視覚的に使いやすいもの 【 契約金額(税抜) 】 ご希望の単価と合わせて提案ください ※契約金額(税込)からシステム利用料を差し引いた金額が、ワーカーさまの受取金額となります その他ご質問等ありましたら、気軽にお問い合わせください。 ご応募をお待ちしております! |
予約ボタンが鮮明だった点、シンプルの中にきれいさがあった点を評価し、この度は選ばせていただきました。
大変多くの数のご応募くださりありがとうございました!今後、似たような形でデザイン制作の募集等をする予定のため、また機会があればよろしくお願いいたします。

```html
<!DOCTYPE html>
<html lang="ja">
<head>
<meta charset="utf-8">
<title>クリニック リッチメニュー</title>
<link rel="stylesheet" href="https://fonts.googleapis.com/css2?family=Noto+Sans+JP:wght@500&display=swap">
<style>
  :root {
    --canvas: #ecece6;
    --blue: #7b97c0;
    --white: #ffffff;
  }
  * { box-sizing: border-box; margin: 0; padding: 0; }
  html, body { width: 1200px; height: 810px; overflow: hidden; background: var(--canvas); }
  .menu {
    width: 1200px; height: 810px;
    padding: 24px;
    display: grid;
    grid-template-columns: repeat(3, 1fr);
    grid-template-rows: repeat(2, 1fr);
    gap: 28px;
    font-family: "Noto Sans JP", sans-serif;
  }
  .tile {
    position: relative;
    display: block;
    text-decoration: none;
    overflow: hidden;
  }
  .tile--light { background: var(--white); color: var(--blue); --tile: var(--white); --ink: var(--blue); }
  .tile--dark  { background: var(--blue);  color: var(--white); --tile: var(--blue);  --ink: var(--white); }
  .tile__frame {
    position: absolute; inset: 12px;
    border: 2px solid var(--ink);
  }
  .tile__icon {
    position: absolute; left: 50%; top: 76px;
    width: 160px; height: 160px;
    transform: translateX(-50%);
  }
  .tile__label {
    position: absolute; left: 0; right: 0; top: 266px;
    text-align: center;
    font-size: 29px; font-weight: 500; letter-spacing: 0.06em;
    line-height: 40px;
  }
  .tile__corner {
    position: absolute; right: 12px; bottom: 12px;
    width: 62px; height: 62px;
  }
</style>
</head>
<body>
<nav class="menu">

  <a class="tile tile--light" href="#reserve">
    <span class="tile__frame"></span>
    <svg class="tile__icon" viewBox="0 0 160 160" aria-hidden="true">
      <rect x="50" y="4" width="60" height="152" rx="10" fill="var(--ink)"/>
      <rect x="58" y="20" width="44" height="110" fill="var(--tile)"/>
      <circle cx="80" cy="143" r="5" fill="var(--tile)"/>
    </svg>
    <span class="tile__label">Web受付・予約</span>
    <svg class="tile__corner" viewBox="0 0 62 62" aria-hidden="true">
      <polygon points="62,0 62,62 0,62" fill="var(--ink)"/>
      <line x1="26" y1="58" x2="58" y2="26" stroke="var(--tile)" stroke-width="2"/>
    </svg>
  </a>

  <a class="tile tile--dark" href="#wifi">
    <span class="tile__frame"></span>
    <svg class="tile__icon" viewBox="0 0 160 160" fill="none" stroke="var(--ink)" stroke-width="13" stroke-linecap="round" aria-hidden="true">
      <path d="M14 62 A94 94 0 0 1 146 62"/>
      <path d="M36 84 A62 62 0 0 1 124 84"/>
      <path d="M58 106 A31 31 0 0 1 102 106"/>
      <circle cx="80" cy="130" r="9" fill="var(--ink)" stroke="none"/>
    </svg>
    <span class="tile__label">Free Wi-Fi</span>
    <svg class="tile__corner" viewBox="0 0 62 62" aria-hidden="true">
      <polygon points="62,0 62,62 0,62" fill="var(--ink)"/>
      <line x1="26" y1="58" x2="58" y2="26" stroke="var(--tile)" stroke-width="2"/>
    </svg>
  </a>

  <a class="tile tile--light" href="#site">
    <span class="tile__frame"></span>
    <svg class="tile__icon" viewBox="0 0 160 160" aria-hidden="true">
      <rect x="14" y="28" width="132" height="106" rx="6" fill="var(--ink)"/>
      <rect x="24" y="54" width="112" height="70" fill="var(--tile)"/>
      <circle cx="104" cy="41" r="4.5" fill="var(--tile)"/>
      <circle cx="118" cy="41" r="4.5" fill="var(--tile)"/>
      <circle cx="132" cy="41" r="4.5" fill="var(--tile)"/>
      <rect x="36" y="68" width="88" height="11" fill="var(--ink)"/>
      <rect x="36" y="90" width="44" height="9" fill="var(--ink)"/>
    </svg>
    <span class="tile__label">公式サイト</span>
    <svg class="tile__corner" viewBox="0 0 62 62" aria-hidden="true">
      <polygon points="62,0 62,62 0,62" fill="var(--ink)"/>
      <line x1="26" y1="58" x2="58" y2="26" stroke="var(--tile)" stroke-width="2"/>
    </svg>
  </a>

  <a class="tile tile--dark" href="#calendar">
    <span class="tile__frame"></span>
    <svg class="tile__icon" viewBox="0 0 160 160" aria-hidden="true">
      <rect x="26" y="30" width="108" height="110" rx="6" fill="none" stroke="var(--ink)" stroke-width="7"/>
      <rect x="26" y="30" width="108" height="24" fill="var(--ink)"/>
      <rect x="48" y="16" width="8" height="24" rx="3" fill="var(--ink)"/>
      <rect x="104" y="16" width="8" height="24" rx="3" fill="var(--ink)"/>
      <g fill="var(--ink)">
        <rect x="44" y="66" width="13" height="11"/><rect x="66" y="66" width="13" height="11"/><rect x="88" y="66" width="13" height="11"/><rect x="110" y="66" width="13" height="11"/>
        <rect x="44" y="87" width="13" height="11"/><rect x="66" y="87" width="13" height="11"/><rect x="88" y="87" width="13" height="11"/><rect x="110" y="87" width="13" height="11"/>
        <rect x="44" y="108" width="13" height="11"/><rect x="66" y="108" width="13" height="11"/><rect x="88" y="108" width="13" height="11"/><rect x="110" y="108" width="13" height="11"/>
      </g>
    </svg>
    <span class="tile__label">診療カレンダー</span>
    <svg class="tile__corner" viewBox="0 0 62 62" aria-hidden="true">
      <polygon points="62,0 62,62 0,62" fill="var(--ink)"/>
      <line x1="26" y1="58" x2="58" y2="26" stroke="var(--tile)" stroke-width="2"/>
    </svg>
  </a>

  <a class="tile tile--light" href="#faq">
    <span class="tile__frame"></span>
    <svg class="tile__icon" viewBox="0 0 160 160" aria-hidden="true">
      <g fill="var(--tile)" stroke="var(--ink)" stroke-width="4" stroke-linejoin="round">
        <path d="M47 104 L34 124 L62 108 A38 38 0 1 0 47 104 Z"/>
        <path d="M128 122 L132 146 L110 128 A36 36 0 1 1 128 122 Z"/>
      </g>
      <g fill="var(--ink)" font-family="Noto Sans JP, sans-serif" font-size="28" font-weight="500" text-anchor="middle">
        <text x="64" y="82">Q</text>
        <text x="107" y="104">A</text>
      </g>
    </svg>
    <span class="tile__label">よくある質問</span>
    <svg class="tile__corner" viewBox="0 0 62 62" aria-hidden="true">
      <polygon points="62,0 62,62 0,62" fill="var(--ink)"/>
      <line x1="26" y1="58" x2="58" y2="26" stroke="var(--tile)" stroke-width="2"/>
    </svg>
  </a>

  <a class="tile tile--dark" href="#contact">
    <span class="tile__frame"></span>
    <svg class="tile__icon" viewBox="0 0 160 160" aria-hidden="true">
      <g transform="translate(30 30) scale(4.6)">
        <path fill="var(--ink)" d="M6.62 10.79c1.44 2.83 3.76 5.14 6.59 6.59l2.2-2.2c.27-.27.67-.36 1.02-.24 1.12.37 2.33.57 3.57.57.55 0 1 .45 1 1V20c0 .55-.45 1-1 1-9.39 0-17-7.61-17-17 0-.55.45-1 1-1h3.5c.55 0 1 .45 1 1 0 1.25.2 2.45.57 3.57.11.35.03.74-.25 1.02l-2.2 2.2z" transform="translate(24 0) scale(-1 1)"/>
      </g>
      <g fill="none" stroke="var(--ink)" stroke-width="5" stroke-linecap="round">
        <path d="M104 28 A18 18 0 0 1 118 46"/>
        <path d="M106 14 A32 32 0 0 1 132 40"/>
      </g>
    </svg>
    <span class="tile__label">お問い合わせ</span>
    <svg class="tile__corner" viewBox="0 0 62 62" aria-hidden="true">
      <polygon points="62,0 62,62 0,62" fill="var(--ink)"/>
      <line x1="26" y1="58" x2="58" y2="26" stroke="var(--tile)" stroke-width="2"/>
    </svg>
  </a>

</nav>
</body>
</html>
```